Existing Website Requiring new Pages

I have an existing word press website that was built using elementor.
Website: www.quorvanecare.com.au
I require the Vacancies page (https://www.tallowmerecare.com.au/vacancies/) to be modified to display our new properties along with minor tweaks to how the information is presented.
The vacancies to be displayed are the exactly the same as those that are located on the homepage of QDA website (https://qda.org.au/)
The new pages that link off the Vacancies tab will require custom design.
There are roughly 8 pages/properties to be incorporated. i wish for the design to be very similar to that displayed in the following link; https://www.zomplex.com.au/vacancies/merrylands
Along with this the back end has not been updated for the last 3 years so it also requires some maintenance.
Website is in the disability industry and the custom pages will display information relative to Property Vacancies.
I have attached a ZIP file with some design guides, the information for each of the properties (which will need to be modified to show our business name Quorvane Healthcare) and the example of how it is to look based off the Zomplex website.
If you guys have any suggestions or ideas on how to make this more presentable or possible i'm open to your ideas.
People looking for SDA properties custom built for people with a disability
Disability
Coded - Design and coding required
5+ page

```html
<!DOCTYPE html>
<html lang="en">
<head>
<meta charset="utf-8">
<title>Quorvane Healthcare – SDA Vacancies</title>
<link href="https://fonts.googleapis.com/css2?family=Montserrat:wght@500;600;700;800&family=Open+Sans:wght@400;600;700&display=swap" rel="stylesheet">
<style>
:root{
  --purple:#7a2a8e;
  --purple-2:#a02c84;
  --teal:#127c70;
  --maroon:#8a1c3c;
  --blue:#1f5b8e;
  --orange:#ea7048;
  --ink:#1f2330;
  --muted:#5d6270;
  --line:#e3e5ea;
  --pill:#eef0f3;
  --dark:#23252b;
  --white:#ffffff;
}
*{box-sizing:border-box;margin:0;padding:0}
html,body{width:1200px;height:4264px;overflow:hidden}
body{font-family:"Open Sans",Arial,sans-serif;color:var(--ink);background:var(--white);position:relative}
h1,h2,h3,h4{font-family:"Montserrat",Arial,sans-serif}

/* header */
.site-header{position:absolute;top:0;left:0;width:1200px;height:180px;display:flex;align-items:center;justify-content:space-between;padding:0 60px 0 100px}
.brand{display:flex;align-items:center;gap:12px}
.brand-dot{width:44px;height:44px;border-radius:50%;background:var(--purple-2)}
.brand-name{font-family:"Montserrat",sans-serif;font-weight:700;font-size:22px;color:var(--purple);line-height:1.1;width:160px}
.main-nav{display:flex;gap:34px}
.main-nav a{font-family:"Montserrat",sans-serif;font-size:14px;font-weight:600;color:var(--ink);text-decoration:none;letter-spacing:.5px;padding-bottom:6px}
.main-nav a.active{color:var(--purple-2);border-bottom:2px solid var(--purple-2)}

/* hero */
.hero{position:absolute;top:180px;left:0;width:1200px;height:440px;display:flex}
.hero-panel{width:610px;height:100%;background:linear-gradient(120deg,var(--purple),var(--purple-2));color:var(--white);padding:60px 30px 0 100px}
.hero-panel h1{font-size:30px;font-weight:800;line-height:1.25;margin-bottom:22px;white-space:nowrap}
.hero-panel p{font-size:14px;line-height:1.7;max-width:460px;opacity:.95}
.hero-photo{flex:1;background:linear-gradient(135deg,#c9c2b8,#8f8a84 55%,#e7dfd2)}

/* search */
.search-bar{position:absolute;top:530px;left:100px;width:1000px;height:116px;background:var(--white);box-shadow:0 10px 30px rgba(0,0,0,.12);display:flex;align-items:flex-end;gap:20px;padding:0 28px 26px}
.field{width:220px}
.field label{display:block;font-family:"Montserrat",sans-serif;font-size:12px;font-weight:700;margin-bottom:8px}
.select{height:42px;border:1px solid var(--line);border-radius:3px;display:flex;align-items:center;justify-content:space-between;padding:0 14px;font-size:13px;color:var(--muted)}
.select svg{width:10px;height:10px}
.btn{display:inline-flex;align-items:center;justify-content:center;font-family:"Montserrat",sans-serif;font-weight:700;border-radius:3px;text-decoration:none}
.btn-submit{width:190px;height:42px;margin-left:auto;background:var(--orange);color:var(--white);font-size:14px}

/* map */
.map{position:absolute;top:692px;left:100px;width:1000px;height:468px;background:linear-gradient(160deg,#e9ecdf,#d9e6ee 55%,#cfe0ea)}

/* locations */
.locations-band{position:absolute;top:1232px;left:0;width:1200px;height:290px;background:var(--teal)}
.locations-title{position:absolute;top:1268px;left:100px;font-size:36px;font-weight:800;color:var(--white)}
.card-grid{position:absolute;top:1372px;left:100px;width:1000px;display:grid;grid-template-columns:repeat(3,312px);column-gap:32px;row-gap:32px}
.card{height:464px;background:var(--white)}
.card-photo{height:268px;background:linear-gradient(180deg,#a9c4df,#d9d4cc 55%,#8a8580)}
.card-photo.alt{background:linear-gradient(180deg,#b6cde4,#bcb5aa 50%,#6e6a66)}
.card-photo.interior{background:linear-gradient(180deg,#eef0ec,#c7d6cf 60%,#a9b7b2)}
.card-body{padding:16px 0 0}
.card-title{font-size:14px;font-weight:700;text-transform:uppercase;margin-bottom:4px}
.card-place{font-size:14px;color:var(--orange);margin-bottom:12px}
.tags{display:flex;flex-wrap:wrap;gap:8px;margin-bottom:14px}
.tag{font-size:12px;font-weight:600;background:var(--pill);padding:5px 10px;border-radius:3px}
.btn-details{height:36px;padding:0 18px;background:var(--orange);color:var(--white);font-size:12px;letter-spacing:.4px}

/* discover */
.discover{position:absolute;top:2905px;left:0;width:1200px;height:375px;display:flex}
.discover-panel{width:720px;background:var(--maroon);color:var(--white);padding:54px 50px 0 100px}
.discover-panel h2{font-size:34px;font-weight:800;line-height:1.2;margin-bottom:22px}
.discover-panel p{font-size:14px;line-height:1.7}
.discover-photo{flex:1;background:linear-gradient(135deg,#e7d6c6,#c9a58e 50%,#7b8f5c)}

/* faq */
.faq{position:absolute;top:3330px;left:100px;width:1000px}
.faq h2{font-size:32px;font-weight:700;margin-bottom:40px}
.faq-list{display:grid;grid-template-columns:460px 500px;column-gap:40px;row-gap:32px}
.faq-item{height:64px;border:1px solid var(--line);border-left:4px solid var(--orange);display:flex;align-items:center;justify-content:space-between;padding:0 20px;font-size:15px;font-weight:600}
.faq-item span.plus{color:var(--orange);font-size:26px;font-weight:400}

/* cta */
.cta{position:absolute;top:3632px;left:0;width:1200px;height:280px;background:var(--blue);color:var(--white);text-align:center;padding-top:62px}
.cta h2{font-size:36px;font-weight:700;margin-bottom:18px}
.cta p{font-size:14px;margin-bottom:30px}
.cta-actions{display:flex;gap:20px;justify-content:center}
.btn-enquire{width:170px;height:50px;background:var(--orange);color:var(--white);font-size:15px}
.btn-learn{width:170px;height:50px;border:2px solid var(--white);color:var(--white);font-size:15px}

/* footer */
.site-footer{position:absolute;top:3930px;left:0;width:1200px;height:290px;padding:32px 100px 0;display:flex}
.footer-brand{width:420px}
.footer-brand .brand{margin-bottom:22px}
.contact-line{display:flex;align-items:center;gap:10px;font-size:12px;color:var(--muted);margin-bottom:8px}
.contact-line svg{width:14px;height:14px;flex:none}
.socials{width:80px;display:flex;flex-direction:column;gap:14px;padding-top:40px}
.socials span{width:28px;height:28px;border-radius:50%;background:var(--blue)}
.footer-col{border-left:1px solid var(--line);padding:10px 0 0 26px;width:250px}
.footer-col h4{font-size:13px;font-weight:700;text-transform:uppercase;margin-bottom:14px}
.footer-col li{list-style:none;font-size:12px;color:var(--muted);margin-bottom:8px}
.copyright{position:absolute;top:4220px;left:0;width:1200px;height:44px;background:var(--dark);color:#b8bbc4;font-size:12px;display:flex;align-items:center;justify-content:center}
</style>
</head>
<body>

<header class="site-header">
  <div class="brand"><span class="brand-dot"></span><span class="brand-name">Quorvane Healthcare</span></div>
  <nav class="main-nav">
    <a href="#">HOME</a><a href="#">ABOUT US</a><a href="#" class="active">WHAT WE DO</a><a href="#">REFERRALS</a><a href="#">FEEDBACK</a><a href="#">CONTACT US</a>
  </nav>
</header>

<section class="hero">
  <div class="hero-panel">
    <h1>Specialist Disability<br>Accommodation Properties</h1>
    <p>Lorem ipsum dolor sit amet, consectetur adipiscing elit, sed do eiusmod tempor incididunt ut labore et dolore magna aliqua. Ut enim ad minim veniam.</p>
  </div>
  <div class="hero-photo" role="img" aria-label="Photo of a woman working on a laptop at a home desk"></div>
</section>

<form class="search-bar">
  <div class="field"><label>CURRENT SDA FUTURE</label><div class="select">Both type<svg viewBox="0 0 10 10"><path d="M1 3l4 4 4-4" fill="none" stroke="#5d6270" stroke-width="1.5"/></svg></div></div>
  <div class="field"><label>DESIGN CATEGORY</label><div class="select">All Categories<svg viewBox="0 0 10 10"><path d="M1 3l4 4 4-4" fill="none" stroke="#5d6270" stroke-width="1.5"/></svg></div></div>
  <div class="field"><label>LOCATION</label><div class="select">All Categories<svg viewBox="0 0 10 10"><path d="M1 3l4 4 4-4" fill="none" stroke="#5d6270" stroke-width="1.5"/></svg></div></div>
  <span class="btn btn-submit">Submit</span>
</form>

<div class="map" role="img" aria-label="Map of Sydney suburbs showing property locations"></div>

<div class="locations-band"></div>
<h2 class="locations-title">Available Locations (9)</h2>

<section class="card-grid">
  <article class="card"><div class="card-photo" role="img" aria-label="Photo of the Greystanes house"></div><div class="card-body"><h3 class="card-title">SDA in Greystanes</h3><p class="card-place">Greystanes</p><div class="tags"><span class="tag">Fully Accessible</span><span class="tag">High Physical Support</span></div><span class="btn btn-details">VIEW DETAILS</span></div></article>
  <article class="card"><div class="card-photo alt" role="img" aria-label="Photo of the Jordan Springs house"></div><div class="card-body"><h3 class="card-title">SDA in Jordan Springs</h3><p class="card-place">Jordan Springs</p><div class="tags"><span class="tag">Fully Accessible</span><span class="tag">Improved Liveability</span></div><span class="btn btn-details">VIEW DETAILS</span></div></article>
  <article class="card"><div class="card-photo alt" role="img" aria-label="Photo of the Werrington townhouse"></div><div class="card-body"><h3 class="card-title">SDA in Werrington</h3><p class="card-place">Werrington</p><div class="tags"><span class="tag">Fully Accessible</span><span class="tag">Improved Liveability</span></div><span class="btn btn-details">VIEW DETAILS</span></div></article>
  <article class="card"><div class="card-photo" role="img" aria-label="Photo of the Wentworthville villas"></div><div class="card-body"><h3 class="card-title">SDA Villas in Wentworthville</h3><p class="card-place">Wentworthville</p><div class="tags"><span class="tag">Fully Accessible</span><span class="tag">High Physical Support</span><span class="tag">Improved Liveability</span></div><span class="btn btn-details">VIEW DETAILS</span></div></article>
  <article class="card"><div class="card-photo alt" role="img" aria-label="Photo of the West Pennant Hills house"></div><div class="card-body"><h3 class="card-title">SDA in West Pennant Hills</h3><p class="card-place">West Pennant Hills</p><div class="tags"><span class="tag">Fully Accessible</span><span class="tag">High Physical Support</span></div><span class="btn btn-details">VIEW DETAILS</span></div></article>
  <article class="card"><div class="card-photo" role="img" aria-label="Photo of the Guildford West house"></div><div class="card-body"><h3 class="card-title">SDA in Guildford West</h3><p class="card-place">Guildford West</p><div class="tags"><span class="tag">Fully Accessible</span><span class="tag">High Physical Support</span></div><span class="btn btn-details">VIEW DETAILS</span></div></article>
  <article class="card"><div class="card-photo interior" role="img" aria-label="Photo of the Austral property kitchen"></div><div class="card-body"><h3 class="card-title">SDA in Austral</h3><p class="card-place">Austral</p><div class="tags"><span class="tag">Fully Accessible</span><span class="tag">High Physical Support</span><span class="tag">Robust</span></div><span class="btn btn-details">VIEW DETAILS</span></div></article>
  <article class="card"><div class="card-photo alt" role="img" aria-label="Photo of the Merrylands townhouses"></div><div class="card-body"><h3 class="card-title">SDA in Merrylands</h3><p class="card-place">Merrylands</p><div class="tags"><span class="tag">Fully Accessible</span><span class="tag">High Physical Support</span></div><span class="btn btn-details">VIEW DETAILS</span></div></article>
  <article class="card"><div class="card-photo" role="img" aria-label="Photo of the Blacktown house"></div><div class="card-body"><h3 class="card-title">SDA in Blacktown</h3><p class="card-place">Blacktown</p><div class="tags"><span class="tag">Fully Accessible</span><span class="tag">High Physical Support</span></div><span class="btn btn-details">VIEW DETAILS</span></div></article>
</section>

<section class="discover">
  <div class="discover-panel">
    <h2>Discover Specialist<br>Disability Accommodation<br>with Quorvane Healthcare</h2>
    <p>Ut enim ad minim veniam, quis nostrud exercitation ullamco laboris nisi ut aliquip ex ea commodo consequat. Duis aute irure dolor in reprehenderit in voluptate velit esse cillum dolore eu fugiat nulla pariatur. Excepteur sint occaecat cupidatat non proident, sunt in culpa qui officia deserunt mollit anim id est laborum.</p>
  </div>
  <div class="discover-photo" role="img" aria-label="Photo of a smiling family outdoors"></div>
</section>

<section class="faq">
  <h2>Frequently Asked Questions</h2>
  <div class="faq-list">
    <div class="faq-item">Who qualifies for SDA Accomodation?<span class="plus">+</span></div>
    <div class="faq-item">What are the available services?<span class="plus">+</span></div>
    <div class="faq-item">Why should we choose Quorvane Healthcare?<span class="plus">+</span></div>
    <div class="faq-item">Can I visit the Healthcare center before deciding?<span class="plus">+</span></div>
  </div>
</section>

<section class="cta">
  <h2>Get in touch with our experts today</h2>
  <p>Get started now or chat to someone from our team today.</p>
  <div class="cta-actions"><span class="btn btn-enquire">Enquire Now</span><span class="btn btn-learn">Learn More</span></div>
</section>

<footer class="site-footer">
  <div class="footer-brand">
    <div class="brand"><span class="brand-dot"></span><span class="brand-name">Quorvane Healthcare</span></div>
    <p class="contact-line"><svg viewBox="0 0 14 14"><rect x="1" y="3" width="12" height="8" fill="none" stroke="#a02c84" stroke-width="1.3"/><path d="M1 3l6 5 6-5" fill="none" stroke="#a02c84" stroke-width="1.3"/></svg>Email: info@quorvanecare.com.au</p>
    <p class="contact-line"><svg viewBox="0 0 14 14"><path d="M3 1h3l1 3-2 1a7 7 0 0 0 4 4l1-2 3 1v3c0 1-1 2-2 2A11 11 0 0 1 1 3c0-1 1-2 2-2z" fill="#a02c84"/></svg>Phone: +61 2 9000 4821</p>
    <p class="contact-line"><svg viewBox="0 0 14 14"><circle cx="7" cy="7" r="6" fill="none" stroke="#a02c84" stroke-width="1.3"/><path d="M7 3v4l3 2" fill="none" stroke="#a02c84" stroke-width="1.3"/></svg>Operating Hours: 9AM to 5PM Monday – Friday</p>
  </div>
  <div class="socials"><span></span><span></span><span></span><span></span></div>
  <div class="footer-col">
    <h4>Accommodation</h4>
    <ul><li>Supported Independent Living (SIL)</li><li>Specialist Disability Accommodation (SDA)</li><li>Short-term Accommodation (Respite)</li><li>Vacancies</li></ul>
  </div>
  <div class="footer-col">
    <h4>What We Do</h4>
    <ul><li>In Home Care</li><li>Social &amp; Community Services</li><li>Therapeutic Supports</li><li>Support Coordination</li><li>Allied Healthcare</li></ul>
  </div>
</footer>
<div class="copyright">© Copyright 2024 Quorvane Healthcare. All Rights Reserved.</div>

</body>
</html>
```